Child Care Centre needs new roadside billboard / sign*

We have a 2400mm x 1200mm sign that needs to be refreshed. The design is dated and we want to create a new cleaner, more readable roadside signIt needs to be readable from about 100m awayThe text requirements are simple, but we need it to have a warm, family feel.We are located in a small beach side community and we have a lot of bright colours in our centre (a lot of blues and yellows)https://www.maplegrovechildcare.com.au/

Target Market(s)

Parents of young children

Industry/Entity Type

Childcare

Colors
fbed22
0355a3

Requirements
Must have
• Readable from c.100m
• Simple, warm design
Should not have
• Cluttered or overly busy

```html
<!DOCTYPE html>
<html lang="en">
<head>
<meta charset="utf-8">
<title>Maple Grove Early Education – Roadside Sign</title>
<link href="https://fonts.googleapis.com/css2?family=Montserrat:wght@600&family=Quicksand:wght@500;700&display=swap" rel="stylesheet">
<style>
  :root {
    --page: #ffffff;
    --sign: #ffffff;
    --magenta: #b52a8f;
    --green: #06a14f;
    --pink: #e6306f;
    --sky: #13a8e8;
    --ink: #1b1b1b;
    --mascot-yellow: #f4e628;
    --mascot-grey: #9a9a9a;
  }
  * { margin: 0; padding: 0; box-sizing: border-box; }
  html, body {
    width: 1200px;
    height: 720px;
    overflow: hidden;
    background: var(--page);
  }
  .sign {
    position: absolute;
    left: 40px;
    top: 80px;
    width: 1120px;
    height: 560px;
    background: var(--sign);
  }
  .age-band {
    position: absolute;
    left: 23px;
    top: 24px;
    width: 1074px;
    height: 72px;
    background: var(--magenta);
    color: #fff;
    font-family: "Montserrat", sans-serif;
    font-weight: 600;
    font-size: 45px;
    line-height: 72px;
    text-align: center;
    letter-spacing: 0.2px;
  }
  .mascot {
    position: absolute;
    left: 25px;
    top: 118px;
    width: 230px;
    height: 335px;
  }
  .brand {
    position: absolute;
    right: 25px;
    top: 128px;
    text-align: right;
    font-family: "Quicksand", sans-serif;
    font-weight: 700;
    color: var(--ink);
    line-height: 1;
  }
  .brand-name { font-size: 62px; display: block; }
  .brand-sub { font-size: 46px; display: block; margin-top: 8px; }
  .services {
    position: absolute;
    right: 25px;
    top: 270px;
    font-family: "Quicksand", sans-serif;
    font-weight: 500;
    font-size: 35px;
    color: var(--ink);
    white-space: nowrap;
  }
  .services .before { color: var(--pink); }
  .services .after { color: var(--sky); }
  .services .vacation { color: var(--green); }
  .services .star { width: 22px; height: 22px; vertical-align: -1px; margin: 0 8px; }
  .phone {
    position: absolute;
    right: 25px;
    top: 348px;
    font-family: "Quicksand", sans-serif;
    font-weight: 700;
    font-size: 84px;
    color: var(--magenta);
    letter-spacing: 1px;
    word-spacing: 12px;
    white-space: nowrap;
  }
  .hours-band {
    position: absolute;
    left: 23px;
    top: 476px;
    width: 1074px;
    height: 58px;
    background: var(--green);
    color: #fff;
    font-family: "Quicksand", sans-serif;
    font-weight: 700;
    font-size: 46px;
    line-height: 56px;
    padding-left: 25px;
    white-space: nowrap;
  }
</style>
</head>
<body>
  <main class="sign">
    <div class="age-band">6 WEEKS TO 6 YEARS (LONG DAY CARE)</div>

    <svg class="mascot" role="img" aria-label="Cartoon seahorse mascot in a graduation cap holding a diploma" viewBox="0 0 230 335">
      <defs>
        <linearGradient id="mascotTone" x1="0" y1="0" x2="0" y2="1">
          <stop offset="0" stop-color="var(--mascot-grey)"/>
          <stop offset="0.18" stop-color="var(--mascot-yellow)"/>
          <stop offset="1" stop-color="var(--mascot-yellow)"/>
        </linearGradient>
      </defs>
      <rect x="0" y="0" width="230" height="335" rx="24" fill="url(#mascotTone)"/>
    </svg>

    <div class="brand">
      <span class="brand-name">Maple Grove</span>
      <span class="brand-sub">Early Education</span>
    </div>

    <p class="services">
      <span class="before">Before</span> and <span class="after">After</span> School Care<svg class="star" viewBox="0 0 24 24" aria-hidden="true"><polygon points="12,1 15,9 23,9 16.5,14 19,22 12,17 5,22 7.5,14 1,9 9,9" fill="var(--magenta)"/></svg><span class="vacation">Vacation</span> Care
    </p>

    <p class="phone">07 4150 2386</p>

    <div class="hours-band">Open 6.30 am – 6.30 pm - 52 weeks a year</div>
  </main>
</body>
</html>
```